Harbourline Blinds & Shutters

It Needs to look classy as my target is the upper end of the blind market
I need a Logo design on front and description on back of what i do:
- Roller Blinds
- Vertical Blinds
- Venetian Blinds
- Plantation Shutters
- Aluminum External Shutters
and contact details
Gavin
0418527306
and
Terry
0421690358
Updates
Hi Guys,
Sorry for the no feedback but i was waiting on my logo design. But its done now i have uploaded it. so if you could take a look and send through some designs
Reason: my logo was just finished an i just uploaded it today really dont understand why my deadline has been rached foe my bizcards as it states no deadline. But please extend
Target Market(s)
People that live on the coast and are looking for classy good quality blinds and shutters
Font styles to use
Other font styles liked:
- Copperplate Gothic,open to suggestion
Look and feel
Each slider illustrates characteristics of the customer's brand and the style your logo design should communicate.

```html
<!DOCTYPE html>
<html lang="en">
<head>
<meta charset="utf-8">
<title>Harbourline Blinds &amp; Shutters – Business Cards</title>
<link href="https://fonts.googleapis.com/css2?family=Josefin+Sans:wght@300;400&display=swap" rel="stylesheet">
<style>
  :root {
    --backdrop: #e9e6e1;
    --card-black: #0b0b0b;
    --card-charcoal: #1c1c1c;
    --gold: #c9a544;
    --gold-light: #e8cf7c;
    --gold-dark: #8a6a22;
    --silver: #d9d9d9;
    --list-grey: #cfcfcf;
  }
  * { box-sizing: border-box; margin: 0; padding: 0; }
  html, body {
    width: 1200px;
    height: 784px;
    overflow: hidden;
    background: var(--backdrop);
    font-family: "Josefin Sans", sans-serif;
  }
  .sheet {
    position: relative;
    width: 1200px;
    height: 784px;
    display: flex;
    align-items: center;
    justify-content: center;
    gap: 40px;
  }
  .card {
    position: relative;
    width: 540px;
    height: 309px;
    overflow: hidden;
    box-shadow: 0 8px 24px rgba(0,0,0,0.25);
  }

  /* Back of card */
  .card--back {
    background: radial-gradient(ellipse at 55% 40%, var(--card-charcoal) 0%, var(--card-black) 75%);
  }
  .contact {
    position: absolute;
    top: 30px;
    color: var(--gold);
    font-weight: 300;
    text-align: center;
  }
  .contact--left { left: 42px; }
  .contact--right { right: 42px; }
  .contact__name { font-size: 19px; letter-spacing: 0.5px; }
  .contact__phone { font-size: 21px; letter-spacing: 1.5px; margin-top: 2px; }
  .services {
    position: absolute;
    top: 112px;
    left: 0;
    width: 100%;
    list-style: none;
    text-align: center;
    color: var(--list-grey);
    font-weight: 300;
    font-size: 15px;
    line-height: 24px;
  }

  /* Front of card */
  .card--front { background: var(--card-black); }
  .damask {
    position: absolute;
    inset: 0;
    background: radial-gradient(ellipse at 50% 50%, #262626 0%, #141414 60%, #080808 100%);
  }
  .band {
    position: absolute;
    left: 0;
    top: 118px;
    width: 100%;
    height: 86px;
    background: var(--card-black);
    border-top: 2px solid var(--gold);
    border-bottom: 2px solid var(--gold);
  }
  .ornament {
    position: absolute;
    left: 50%;
    width: 150px;
    height: 52px;
    transform: translateX(-50%);
    border-radius: 26px;
    background: radial-gradient(ellipse at 50% 50%, var(--gold-light) 0%, var(--gold) 45%, var(--gold-dark) 100%);
    opacity: 0.9;
  }
  .ornament--top { top: 60px; }
  .ornament--bottom { top: 210px; }
  .wordmark {
    position: absolute;
    left: 0;
    top: 128px;
    width: 100%;
    text-align: center;
    color: var(--silver);
    font-weight: 300;
  }
  .wordmark__name { display: block; font-size: 40px; letter-spacing: 2px; line-height: 44px; }
  .wordmark__sub { display: block; font-size: 16px; letter-spacing: 3px; line-height: 24px; }
</style>
</head>
<body>
  <main class="sheet">
    <section class="card card--back" aria-label="Business card back">
      <div class="contact contact--left">
        <div class="contact__name">Gavin</div>
        <div class="contact__phone">0418527306</div>
      </div>
      <div class="contact contact--right">
        <div class="contact__name">Terry</div>
        <div class="contact__phone">0421690358</div>
      </div>
      <ul class="services">
        <li>Roller Blinds</li>
        <li>Vertical Blinds</li>
        <li>Venetian Blinds</li>
        <li>Plantation Shutters</li>
        <li>Aluminum External Shutters</li>
      </ul>
    </section>

    <section class="card card--front" aria-label="Business card front">
      <div class="damask" role="img" aria-label="Dark charcoal damask floral pattern background"></div>
      <div class="band"></div>
      <div class="ornament ornament--top" role="img" aria-label="Gold baroque scroll ornament"></div>
      <div class="ornament ornament--bottom" role="img" aria-label="Gold baroque scroll ornament"></div>
      <h1 class="wordmark">
        <span class="wordmark__name">Harbourline</span>
        <span class="wordmark__sub">Blinds &amp; Shutters</span>
      </h1>
    </section>
  </main>
</body>
</html>
```